TOVR Enterprise
company business card and envolpe design
TOVR Enterprise -
Creative Brief
Professional
Neeraj Pillai
Director
114, 2c, 2nd floor, Rukminibai Market, Rukminibai Bldg No. 6, Pepper Orchard Lane, Mumbai - 400017.
pillaineeraj41@postvela.example
Should look same as the logo. Business card and Stationery should also be very professional.
TOVR Enterprise is the parent company underwhich many other firms are going to start. So back of the card should be designed in way that i can add the name of other firms.

```html
<!DOCTYPE html>
<html lang="en">
<head>
<meta charset="utf-8">
<title>TOVR Enterprise Stationery</title>
<link href="https://fonts.googleapis.com/css2?family=Montserrat:wght@400;600;800&display=swap" rel="stylesheet">
<style>
:root{
  --board:#2e2e30;
  --paper:#ffffff;
  --red:#b3141b;
  --red-dark:#6e0a0e;
  --ink:#555;
  --faint:#f6eaea;
  --label:#9a9a9a;
}
*{box-sizing:border-box;margin:0;padding:0}
html,body{width:1200px;height:338px;overflow:hidden;background:var(--board);font-family:"Montserrat",sans-serif}
.board{position:relative;width:1200px;height:338px}
.piece{position:absolute;background:var(--paper);overflow:hidden}
.brand{display:flex;align-items:center;gap:3px;color:var(--red);font-weight:800;letter-spacing:.5px;white-space:nowrap}
.brand .dot{border-radius:50%;background:var(--red);flex:none}
.label{position:absolute;color:var(--label);font-size:4px;white-space:nowrap}
.watermark{position:absolute;border-radius:50%;background:var(--faint)}
.contact{position:absolute;color:var(--ink);font-size:3px;line-height:4px;text-align:right;white-space:nowrap}
.band{position:absolute;left:0;right:0;bottom:0;background:linear-gradient(180deg,var(--red),var(--red-dark))}
.band p{color:#fff;font-size:3px;text-align:center;padding-top:4px;white-space:nowrap}

/* business cards */
.card{width:96px;height:31px}
.card-front{left:53px;top:117px}
.card-back{left:53px;top:175px}
.card-firms{left:53px;top:211px}
.card-front .brand{position:absolute;left:5px;top:5px;font-size:6px}
.card-front .brand .dot{width:6px;height:6px}
.card-front .contact{right:4px;top:14px}
.card-back .brand{position:absolute;left:5px;top:10px;font-size:7px}
.card-back .brand .dot{width:8px;height:8px}
.card-firms .row{position:absolute;left:5px;right:5px;top:13px;display:flex;justify-content:space-between}
.card-firms .brand{font-size:4px;gap:2px;letter-spacing:.2px}
.card-firms .brand .dot{width:3px;height:3px}

/* letterheads */
.letter{width:190px;height:293px;top:19px}
.letter-a{left:175px}
.letter-b{left:384px}
.letter .watermark{width:82px;height:82px;left:54px;top:178px}
.letter-a .brand{position:absolute;left:14px;top:14px;font-size:13px}
.letter-a .brand .dot{width:13px;height:13px}
.letter-a .contact{right:14px;top:14px}
.letter-b .brand{position:absolute;left:0;right:0;top:14px;justify-content:center;font-size:13px}
.letter-b .brand .dot{width:13px;height:13px}
.letter-b .band{height:16px}

/* envelopes */
.env{width:230px;height:115px;left:629px}
.env-dl{top:41px}
.env-large{top:173px}
.env .brand{position:absolute;left:10px;top:10px;font-size:11px}
.env .brand .dot{width:11px;height:11px}
.env .sub{position:absolute;left:10px;top:26px;color:var(--ink);font-size:3px;line-height:4px}
.env-large .band{height:10px}
.env-large .watermark{width:60px;height:60px;right:20px;top:22px}

.env-back{left:893px;top:10px;width:288px;height:273px;background:none}
</style>
</head>
<body>
<main class="board">

  <span class="label" style="left:53px;top:110px">Card Front</span>
  <section class="piece card card-front">
    <div class="brand"><span class="dot"></span>TOVR</div>
    <div class="contact">Director<br>Head Office<br>Mumbai, India</div>
  </section>

  <span class="label" style="left:53px;top:168px">Card Back</span>
  <section class="piece card card-back">
    <div class="brand"><span class="dot"></span>TOVR Enterprise</div>
  </section>

  <section class="piece card card-firms">
    <div class="row">
      <div class="brand"><span class="dot"></span>TOVR</div>
      <div class="brand"><span class="dot"></span>TOVR</div>
      <div class="brand"><span class="dot"></span>TOVR</div>
      <div class="brand"><span class="dot"></span>TOVR</div>
    </div>
  </section>

  <section class="piece letter letter-a">
    <div class="brand"><span class="dot"></span>TOVR</div>
    <div class="contact">Head Office, Second Floor<br>Market Building, Orchard Lane<br>Mumbai, India</div>
    <div class="watermark"></div>
  </section>

  <section class="piece letter letter-b">
    <div class="brand"><span class="dot"></span>TOVR</div>
    <div class="watermark"></div>
    <div class="band"><p>Head Office · Market Building · Orchard Lane · Mumbai, India</p></div>
  </section>

  <section class="piece env env-dl">
    <div class="brand"><span class="dot"></span>TOVR</div>
    <div class="sub">TOVR Enterprise<br>Mumbai, India</div>
  </section>
  <span class="label" style="left:730px;top:143px">Envelope Front</span>

  <section class="piece env env-large">
    <div class="brand"><span class="dot"></span>TOVR</div>
    <div class="sub">TOVR Enterprise<br>Mumbai, India</div>
    <div class="watermark"></div>
    <div class="band"></div>
  </section>
  <span class="label" style="left:730px;top:272px">Envelope Large</span>

  <svg class="piece env-back" viewBox="0 0 288 273" aria-hidden="true">
    <defs>
      <linearGradient id="flapRed" x1="0" y1="0" x2="0" y2="1">
        <stop offset="0" stop-color="#e02a30"/><stop offset="1" stop-color="#5e080c"/>
      </linearGradient>
      <linearGradient id="flapGrey" x1="0" y1="0" x2="0" y2="1">
        <stop offset="0" stop-color="#d8d8d8"/><stop offset="1" stop-color="#7a7a7a"/>
      </linearGradient>
    </defs>
    <rect x="0" y="0" width="288" height="58" rx="3" fill="url(#flapRed)"/>
    <rect x="0" y="102" width="288" height="34" rx="3" fill="url(#flapGrey)"/>
    <rect x="0" y="160" width="288" height="106" fill="#fff"/>
    <polyline points="0,160 144,222 288,160" fill="none" stroke="#ddd" stroke-width="1"/>
    <line x1="0" y1="266" x2="118" y2="212" stroke="#ddd"/>
    <line x1="288" y1="266" x2="170" y2="212" stroke="#ddd"/>
  </svg>
  <span class="label" style="left:1080px;top:288px">Envelope Rear</span>

</main>
</body>
</html>
```